New Menu for Elegant Cafe Pastry Shop

We need to choose a design and layout for our new menu. We would like to also condense our current menu to 4-6 pages.
We will be changing prices and items on the menu, so it needs to be editable. Adobe formats are preferred. The size of the pages needs to be letter size. We will be printing it in house
Please take inspiration from the photos of our shop and food and also our Picmosaic page.
Attached are our current menu our logo and the logo info

https://www.picmosaic.com/marbrecoquette/?hl=en
https://maps.wayfindr.app/Qk3Lm9Xp2Tb7VwR4a

Industry/Entity Type

Food Cafe Bakery pastry

Other font styles liked:
• please look at attached files

Colors

Designer to choose colors to be used in the design.

Requirements
Nice to have
• Use of Arches like on our shop wallpaper or oblong eclair shapes, Art Deco elements

```html
<!DOCTYPE html>
<html lang="en">
<head>
<meta charset="UTF-8">
<title>Marbre Coquette — Menu Cover</title>
<link href="https://fonts.googleapis.com/css2?family=Cinzel:wght@400&display=swap" rel="stylesheet">
<style>
  :root {
    --teal: #45c3cc;
    --blush: #f1cdc9;
    --cream: #f3f2ee;
    --plum: #3b1d2f;
    --paper: #ffffff;
  }
  html, body {
    margin: 0;
    padding: 0;
    overflow: hidden;
    background: var(--paper);
  }
  .menu-cover {
    position: relative;
    width: 927px;
    height: 1200px;
    background: var(--paper);
    overflow: hidden;
  }
  .deco-corner {
    position: absolute;
    width: 210px;
    height: 370px;
  }
  .deco-corner--top-left { top: 0; left: 0; }
  .deco-corner--top-right { top: 0; right: 0; transform: scaleX(-1); }
  .deco-corner--bottom-left { bottom: 0; left: 0; transform: scaleY(-1); }
  .deco-corner--bottom-right { bottom: 0; right: 0; transform: scale(-1, -1); }
  .arch-teal { fill: var(--teal); }
  .arch-blush { fill: var(--blush); }
  .arch-cream { fill: var(--cream); }
  .brand-name {
    position: absolute;
    left: 0;
    right: 0;
    top: 570px;
    margin: 0;
    text-align: center;
    font-family: "Cinzel", "Times New Roman", serif;
    font-weight: 400;
    font-size: 42px;
    letter-spacing: 1px;
    color: var(--plum);
  }
</style>
</head>
<body>
<main class="menu-cover">
  <svg class="deco-corner deco-corner--top-left" viewBox="0 0 210 370" aria-hidden="true">
    <path class="arch-teal" d="M0 0H110V314A55 55 0 0 1 0 314Z"/>
    <path class="arch-blush" d="M0 0H106V306A53 53 0 0 1 0 306Z"/>
    <path class="arch-cream" d="M0 60H88V260A44 44 0 0 1 0 260Z"/>
    <path class="arch-blush" d="M106 0H209V172A51.5 51.5 0 0 1 106 172Z"/>
    <path class="arch-teal" d="M106 0H209V162A51.5 51.5 0 0 1 106 162Z"/>
  </svg>
  <svg class="deco-corner deco-corner--top-right" viewBox="0 0 210 370" aria-hidden="true">
    <path class="arch-teal" d="M0 0H110V314A55 55 0 0 1 0 314Z"/>
    <path class="arch-blush" d="M0 0H106V306A53 53 0 0 1 0 306Z"/>
    <path class="arch-cream" d="M0 60H88V260A44 44 0 0 1 0 260Z"/>
    <path class="arch-blush" d="M106 0H209V172A51.5 51.5 0 0 1 106 172Z"/>
    <path class="arch-teal" d="M106 0H209V162A51.5 51.5 0 0 1 106 162Z"/>
  </svg>
  <svg class="deco-corner deco-corner--bottom-left" viewBox="0 0 210 370" aria-hidden="true">
    <path class="arch-blush" d="M0 0H110V314A55 55 0 0 1 0 314Z"/>
    <path class="arch-teal" d="M0 0H106V306A53 53 0 0 1 0 306Z"/>
    <path class="arch-cream" d="M0 60H88V260A44 44 0 0 1 0 260Z"/>
    <path class="arch-teal" d="M106 0H209V172A51.5 51.5 0 0 1 106 172Z"/>
    <path class="arch-blush" d="M106 0H209V162A51.5 51.5 0 0 1 106 162Z"/>
  </svg>
  <svg class="deco-corner deco-corner--bottom-right" viewBox="0 0 210 370" aria-hidden="true">
    <path class="arch-blush" d="M0 0H110V314A55 55 0 0 1 0 314Z"/>
    <path class="arch-teal" d="M0 0H106V306A53 53 0 0 1 0 306Z"/>
    <path class="arch-cream" d="M0 60H88V260A44 44 0 0 1 0 260Z"/>
    <path class="arch-teal" d="M106 0H209V172A51.5 51.5 0 0 1 106 172Z"/>
    <path class="arch-blush" d="M106 0H209V162A51.5 51.5 0 0 1 106 162Z"/>
  </svg>

  <h1 class="brand-name">Marbre Coquette</h1>
</main>
</body>
</html>
```